Long Established Local Fencing (not swords) Business needs fresh Business Cards

We need fresh double sided business cards for our Fencing Construction business, we are looking for something with our new logo design added, and maybe a photo background ?
We recently had cards made from Cardlyne and we were horrified with what we got back, the quality was terrible, so am looking for high quality format for good printing company to make.
We install Steelmora, Timber paling, Aluminium Slat Screening, Picket (timber and aluminium) and most other fencing installations.
Our website is brankelrails.com.au should you like to learn a bit more.
We do have logo in other formats if required.
We have been in business for over 35 years and we have used this as a "motto" it is on our signage

Industry/Entity Type

Construction

Contact Information for Business Card

Open to ideas, we need 3 x different cards, one generic with no name and 2 x others each with 1 of our bosses name on each, I will put into upload files.

Colors
ec1f27
000000
606060
f5f5f5

Requirements
Must have
• Company Name and Logo
• Address
• Contact details, phone, website, email etc
• Small space to write notes when leaving card at residence
Nice to have
• Our motto "Servicing the Peninsula for over 35 years"

```html
<!DOCTYPE html>
<html lang="en">
<head>
<meta charset="utf-8">
<title>Brankel Rails – Business Cards</title>
<link rel="stylesheet" href="https://fonts.googleapis.com/css2?family=Archivo:wght@400;800&family=Arimo:wght@400;700&display=swap">
<style>
  :root {
    --red: #ec1f27;
    --black: #000000;
    --ink: #161616;
    --grey: #606060;
    --paper: #f5f5f5;
    --backdrop: #1c1c1e;
  }
  * { box-sizing: border-box; margin: 0; padding: 0; }
  html, body { width: 1200px; height: 900px; overflow: hidden; }
  body {
    background: var(--backdrop);
    font-family: "Arimo", Arial, sans-serif;
    position: relative;
  }
  .card {
    position: absolute;
    left: 290px;
    width: 620px;
    height: 378px;
    border-radius: 26px;
    overflow: hidden;
    box-shadow: 0 14px 30px rgba(0,0,0,.5);
  }
  /* Front */
  .card-front {
    top: 52px;
    background: linear-gradient(160deg, #ffffff 0%, var(--paper) 60%, #e9e9e9 100%);
  }
  .brand-name {
    font-family: "Archivo", Arial, sans-serif;
    font-weight: 800;
    letter-spacing: 1px;
    line-height: 1;
    display: flex;
    align-items: center;
    gap: 12px;
  }
  .brand-dot {
    width: 18px; height: 18px; border-radius: 50%; background: var(--red);
  }
  .card-front .brand-name {
    position: absolute; left: 44px; top: 40px;
    font-size: 38px; color: var(--ink);
  }
  .person {
    position: absolute; left: 44px; top: 108px;
  }
  .person-name {
    font-family: "Archivo", Arial, sans-serif;
    font-weight: 800; font-size: 20px; color: var(--red); letter-spacing: .5px;
  }
  .person-title { font-size: 14px; color: var(--grey); margin-top: 3px; }
  .rule-red {
    position: absolute; left: 0; top: 160px; width: 300px; height: 2px;
    background: linear-gradient(90deg, var(--grey), var(--red));
  }
  .contact-list {
    position: absolute; left: 44px; top: 176px; list-style: none;
  }
  .contact-list li {
    display: flex; align-items: center; gap: 9px;
    font-size: 14px; color: var(--ink); height: 22px;
  }
  .contact-icon {
    width: 15px; height: 15px; border-radius: 50%; background: var(--red);
    display: flex; align-items: center; justify-content: center;
  }
  .contact-icon svg { width: 9px; height: 9px; }
  .rule-grey {
    position: absolute; left: 0; right: 0; top: 296px; height: 1px; background: #9a9a9a;
  }
  .address {
    position: absolute; right: 36px; bottom: 20px; text-align: right;
    font-size: 14px; color: var(--grey); line-height: 1.3;
  }
  /* Back */
  .card-back {
    top: 470px;
    background: linear-gradient(160deg, #1a1a1a 0%, var(--black) 70%);
  }
  .card-back .brand-name {
    position: absolute; left: 50px; top: 56px; font-size: 52px; color: #ffffff;
  }
  .license {
    position: absolute; left: 52px; top: 130px;
    font-size: 17px; letter-spacing: 5px; color: var(--red);
  }
  .license span { color: #ffffff; }
  .notes-panel {
    position: absolute; left: 40px; right: 40px; top: 200px; bottom: 34px;
    border-radius: 22px;
    background: linear-gradient(170deg, #ffffff, #e4e4e4);
  }
</style>
</head>
<body>
  <section class="card card-front" aria-label="Card front">
    <div class="brand-name"><span class="brand-dot"></span>BRANKEL RAILS</div>
    <div class="person">
      <div class="person-name">DARREN KELLOW</div>
      <div class="person-title">Managing Director</div>
    </div>
    <div class="rule-red"></div>
    <ul class="contact-list">
      <li><span class="contact-icon"><svg viewBox="0 0 10 10"><path d="M2 1l2 2-1 1c.6 1.2 1.6 2.2 2.8 2.8l1-1 2 2-1.3 1.2C4.5 9 1 5.5 .8 2.3z" fill="#fff"/></svg></span>(02) 5550 1842</li>
      <li><span class="contact-icon"><svg viewBox="0 0 10 10"><rect x="3" y="1" width="4" height="8" rx="1" fill="#fff"/></svg></span>0400 555 317</li>
      <li><span class="contact-icon"><svg viewBox="0 0 10 10"><rect x="1" y="2.5" width="8" height="5" fill="#fff"/><path d="M1 2.5l4 3 4-3" stroke="#ec1f27" stroke-width=".8" fill="none"/></svg></span>brankelrails@netmail.com</li>
      <li><span class="contact-icon"><svg viewBox="0 0 10 10"><circle cx="5" cy="5" r="3.6" stroke="#fff" fill="none"/><path d="M1.4 5h7.2M5 1.4c-1.8 2-1.8 5.2 0 7.2M5 1.4c1.8 2 1.8 5.2 0 7.2" stroke="#fff" stroke-width=".7" fill="none"/></svg></span>www.brankelrails.com.au</li>
    </ul>
    <div class="rule-grey"></div>
    <address class="address">PO Box 212<br>Kestrel Point NSW 2260</address>
  </section>

  <section class="card card-back" aria-label="Card back">
    <div class="brand-name"><span class="brand-dot"></span>BRANKEL RAILS</div>
    <div class="license">License No. <span>50127c</span></div>
    <div class="notes-panel" aria-label="Space for notes"></div>
  </section>
</body>
</html>
```